New UI for electricity data tool

We are looking for a new UI for the website http://vantorgrid.net. Reassessing the structure of the website is as important as specific design choices. We have created a uniquely comprehensive set of global electricity generation data and now we are looking for creative solutions for how to make this data accessible. Researching and referencing other similar projects may be a good idea.

Goals:
• The website should clearly communicate the most important general conclusions that can be drawn from the data, including:
◦ The world as a whole is not moving away from fossil fuels for electricity generation
◦ There are substantial differences between regions
▪ Some regions have basically solved the problem – they already generate almost all of their electricity from non-fossil sources
▪ Some regions have greatly improved in terms of decarbonizing their electricity generation.
▪ Some regions have greatly deteriorated, in other words they are using a much higher share of fossil fuels to generate their electricity.
◦ There are substantial differences between energy sources. Regions that have successfully decarbonized their electricity generation have usually done so using hydro and/or nuclear. Other low-carbon energy sources have grown quickly in relative terms in the last few years but are so far contributing little in absolute numbers.
• The website should serve as inspiration for energy policy debates. The goal is to study the impact of existing policies around the world. Energy policy here refers to particular combinations of energy sources – ie how much have the countries invested in each type of electricity generation. The tool should help answer questions such as:
◦ Which countries have done the most in terms of decarbonizing their electricity generation?
◦ Which types of energy polices have lead to the fastest decarbonization processes around the world?
◦ If country A changed its energy policy to be more like country B, what would the likely impact be?

Challenges:
• There is a lot of data – it can be overwhelming to the user. It’s crucial to make the site easy to navigate. The main page should highlight the most important data, and it should also be straightforward to find more detailed data.
• Data availability varies from region to region. The current interface addresses this with the default option “Exclude regions with limited data”. We expect a better approach to dealing with this issue. For some regions and years energy sources are grouped together as for example “other renewables” whereas in other cases more detailed data is available.
• Credibility is crucial. Our data is based on a combination of data from KQ and the Tessary Trust. It must be very clear throughout the site where each data set comes from.

Details:
• The current chart color schemes is loosely based on the carbon emissions from each energy source. This should not necessarily be so. The goal is to on the one hand communicate clearly the amounts of fossil vs non-fossil energy that are generated by each region. At the same time we also want to make it easy to view specific energy sources.

Inspirational websites:
• https://www.grafmelo.org/
• https://trendquarrily.org/

Let's simplify. The main metric to focus on is Brisavolt Index and the extent to which the world and each country has achieved it (eg Iceland 100%, France 88% and so on). I'm considering changing the name of the site to BrisavoltIndex.org. We can use maps, charts and perhaps other tools to communicate this main message. What's the best way of doing this?

```html
<!DOCTYPE html>
<html lang="en">
<head>
<meta charset="utf-8">
<title>BrisavoltIndex.org – Chart</title>
<link rel="stylesheet" href="https://fonts.googleapis.com/css2?family=Lato:wght@400;700&family=Merriweather:wght@700&display=swap">
<style>
:root{
  --ink:#0e2a47;
  --muted:#3c4b5c;
  --soft:#8a96a3;
  --line:#e3e6ea;
  --green:#34d399;
  --green-text:#2bbf86;
  --panel:#f9fafb;
  --panel-dark:#f1f3f5;
  --brazil:#2d7fb8;
  --usa:#8a1ab5;
  --uk:#c0142b;
  --india:#1aae97;
  --china:#c4a62a;
}
*{box-sizing:border-box;margin:0;padding:0}
html,body{width:1200px;height:2269px;overflow:hidden;background:#fff}
body{font-family:"Lato",sans-serif;color:var(--ink)}
.page{position:relative;width:1362px;height:2576px;transform:scale(0.88106);transform-origin:0 0}
.abs{position:absolute}
.serif{font-family:"Merriweather",serif;font-weight:700}

/* header */
.site-header{left:0;top:0;width:1362px;height:134px;border-bottom:2px solid #eef0f2}
.brand{left:52px;top:58px;font-size:29px;font-weight:700;color:var(--green-text);letter-spacing:-.3px}
.nav a{position:absolute;top:64px;font-size:18px;font-weight:700;color:var(--ink);text-decoration:none}
.nav a.active{color:var(--green-text)}
.nav-underline{left:740px;top:131px;width:66px;height:3px;background:var(--green)}
.header-search{left:979px;top:52px;width:331px;height:47px;border:1.5px solid #cfd5db;border-radius:24px}
.header-search span{position:absolute;left:23px;top:13px;font-size:17px;color:#b8c0c8}
.header-search .btn{position:absolute;right:3px;top:3px;width:38px;height:38px;border-radius:50%;background:#2e4a66}

.page-title{left:52px;top:182px;font-size:24px}
.intro{left:52px;top:234px;width:1262px;font-size:14.5px;line-height:25px;color:var(--muted)}

.crumb{left:52px;top:370px;width:262px;height:34px;border:1px solid var(--line);font-size:14.5px;padding:8px 0 0 32px}
.crumb .dim{color:var(--soft)}
.crumb .sep{color:var(--soft);margin:0 14px}
.unit-toggle{left:928px;top:370px;width:382px;height:34px;display:flex;font-size:14.5px}
.unit-toggle div{border:1px solid var(--line);display:flex;align-items:center;justify-content:center}
.unit-toggle .on{border-color:var(--green);background:#ecfbf4;color:var(--green-text)}
.chart-hint{left:0;width:1362px;top:426px;text-align:center;font-size:16.5px;font-weight:700}
.chart-hint u{text-underline-offset:3px}

.chart{left:0;top:470px}
.chart text{font-family:"Lato",sans-serif}

.dl{top:1066px;width:183px;height:34px;background:var(--green);color:#fff;font-size:14.5px;font-weight:700;display:flex;align-items:center;justify-content:center}
.share{left:1050px;top:1074px;font-size:14.5px;font-weight:700;display:flex;align-items:center;gap:16px}
.share .net{display:flex;align-items:center;gap:5px;font-size:13px;color:var(--ink)}
.share .dot{width:8px;height:8px;border-radius:50%;background:var(--ink)}

/* energy sources */
.section-title{font-size:23px}
.hint{font-size:14.5px;font-weight:700}
.box{background:var(--panel)}
.opt{position:absolute;display:flex;align-items:center;gap:14px;font-size:15px;font-weight:700;white-space:nowrap}
.radio{width:22px;height:22px;border-radius:50%;border:1.5px solid #c9ced4;background:#fff;position:relative;flex:none}
.radio.on::after{content:"";position:absolute;left:6px;top:6px;width:7px;height:7px;border-radius:50%;background:var(--ink)}

/* regions */
.regions{left:52px;top:1584px;width:1258px;height:384px;background:var(--panel-dark)}
.reg-search{left:585px;top:1622px;width:223px;height:34px;border:1px solid #cfd5db;background:#fff;font-size:14px;color:#aab3bc;padding:8px 15px}
.reg-sort{left:831px;top:1622px;width:183px;height:34px;border:1px solid #cfd5db;background:#fff;font-size:14.5px;padding:7px 14px}
.check{width:22px;height:22px;border:1.5px solid #c4cad1;background:#fff;border-radius:3px;flex:none;display:flex;align-items:center;justify-content:center}
.check.on{background:var(--ink);border-color:var(--ink)}
.col{position:absolute;top:1698px;display:flex;flex-direction:column;gap:12px}
.col div{display:flex;align-items:center;gap:15px;font-size:15px;font-weight:700;height:22px;white-space:nowrap}
.scroll-track{left:1296px;top:1680px;width:10px;height:288px;background:#e4e7ea}
.scroll-thumb{left:1298px;top:1680px;width:8px;height:56px;background:var(--ink);border-radius:4px}

.concl p{font-size:14.5px;line-height:25px;color:var(--muted)}
.bullets{font-size:14.5px;line-height:26.5px;color:var(--ink)}
.bullets li{list-style:none;position:relative;padding-left:17px;margin-bottom:7px}
.bullets li::before{content:"";position:absolute;left:2px;top:11px;width:5px;height:5px;border-radius:50%;background:var(--ink)}
.bullets li.sub{margin-left:17px}
.bullets li.sub::before{border-radius:0;width:4px;height:4px}

.footer{top:2508px;font-size:14.5px}
.footer a{color:var(--ink);text-underline-offset:3px}
.footer a.mail{color:var(--green-text)}
</style>
</head>
<body>
<div class="page">

<header class="site-header abs">
  <div class="brand abs">BrisavoltIndex.org</div>
  <nav class="nav">
    <a style="left:649px">Map</a>
    <a class="active" style="left:748px">Chart</a>
    <a style="left:857px">Ranking</a>
  </nav>
  <div class="nav-underline abs"></div>
  <div class="header-search abs"><span>Search region</span>
    <div class="btn"><svg width="38" height="38" viewBox="0 0 38 38"><circle cx="18" cy="18" r="7" fill="none" stroke="#fff" stroke-width="2"/><line x1="23" y1="23" x2="27" y2="27" stroke="#fff" stroke-width="2" stroke-linecap="round"/></svg></div>
  </div>
</header>

<h1 class="page-title serif abs">Percentage of low-carbon power source in countries and regions, 1971 to 2018</h1>
<p class="intro abs">Vestibulum malesuada nunc vitae turpis rhoncus suscipit. Nulla volutpat justo quis nulla vehicula hendrerit. Integer ultrices, ante et mollis fringilla, purus arcu finibus nisi, sit amet pretium nisl odio at mauris. Suspendisse consectetur vulputate tellus. Maecenas id dui purus. Morbi nec pellentesque velit, vel finibus felis. Nam sed diam ut risus maximus interdum. Suspendisse in facilisis velit. Lorem ipsum dolor sit amet, consectetur adipiscing elit.</p>

<div class="crumb abs"><span class="dim">Chart</span><span class="sep">&gt;</span><b>5 selected regions</b></div>
<div class="unit-toggle abs"><div style="width:225px">TWh (Absolute Numbers)</div><div class="on" style="width:157px">Percentage (%)</div></div>
<div class="chart-hint abs">Click on a region’s name to view its <u>Region Profile</u></div>

<svg class="chart abs" width="1362" height="560" viewBox="0 470 1362 560">
  <g stroke="#e4e7ea" stroke-width="1">
    <line x1="103" x2="1224" y1="498" y2="498"/><line x1="103" x2="1224" y1="546.3" y2="546.3"/>
    <line x1="103" x2="1224" y1="594.6" y2="594.6"/><line x1="103" x2="1224" y1="642.9" y2="642.9"/>
    <line x1="103" x2="1224" y1="691.2" y2="691.2"/><line x1="103" x2="1224" y1="739.5" y2="739.5"/>
    <line x1="103" x2="1224" y1="787.8" y2="787.8"/><line x1="103" x2="1224" y1="836.1" y2="836.1"/>
    <line x1="103" x2="1224" y1="884.4" y2="884.4"/><line x1="103" x2="1224" y1="932.7" y2="932.7"/>
  </g>
  <line x1="103" x2="1224" y1="981" y2="981" stroke="#c9ced4"/>
  <g font-size="14.5" fill="#0e2a47" text-anchor="end">
    <text x="89" y="503">100%</text><text x="89" y="551">90%</text><text x="89" y="600">80%</text>
    <text x="89" y="648">70%</text><text x="89" y="696">60%</text><text x="89" y="745">50%</text>
    <text x="89" y="793">40%</text><text x="89" y="841">30%</text><text x="89" y="889">20%</text>
    <text x="89" y="938">10%</text><text x="89" y="986">0%</text>
  </g>
  <g font-size="14.5" fill="#0e2a47" text-anchor="middle">
    <text x="103" y="1013">1971</text><text x="199" y="1013">1975</text><text x="318" y="1013">1980</text>
    <text x="437" y="1013">1985</text><text x="556" y="1013">1990</text><text x="676" y="1013">1995</text>
    <text x="795" y="1013">2000</text><text x="914" y="1013">2005</text><text x="1033" y="1013">2010</text>
    <text x="1153" y="1013">2015</text><text x="1224" y="1013">2018</text>
  </g>
  <g transform="translate(103,981) scale(23.851,-4.83)" fill="none" stroke-linejoin="round">
    <g stroke="var(--brazil)">
      <polyline vector-effect="non-scaling-stroke" stroke-width="1.2" points="0,85 1,87.5 2,88.5 3,88.3 4,87.3 5,87.2 6,86.3 7,89 8,90 9,91.8 10,91.3 11,91.6 12,92.5 13,94.7 14,92.8 15,93.7 16,94.6 17,94.6 18,97.5 19,95.5 20,96 21,96.8 22,94.8 23,93 24,92.3 25,93.3 26,93.5 27,93.2 28,91.6 29,90.9 30,90 31,90.2 32,90.2 33,89.8 34,91 35,91.2 36,90.6 37,90 38,90 39,89 40,89 41,89.3 42,86.5 43,85.4 44,86.4 45,87.3 46,87.6 47,88"/>
      <path vector-effect="non-scaling-stroke" stroke-width="4.5" stroke-linecap="round" d="M0 85h0M1 87.5h0M2 88.5h0M3 88.3h0M4 87.3h0M5 87.2h0M6 86.3h0M7 89h0M8 90h0M9 91.8h0M10 91.3h0M11 91.6h0M12 92.5h0M13 94.7h0M14 92.8h0M15 93.7h0M16 94.6h0M17 94.6h0M18 97.5h0M19 95.5h0M20 96h0M21 96.8h0M22 94.8h0M23 93h0M24 92.3h0M25 93.3h0M26 93.5h0M27 93.2h0M28 91.6h0M29 90.9h0M30 90h0M31 90.2h0M32 90.2h0M33 89.8h0M34 91h0M35 91.2h0M36 90.6h0M37 90h0M38 90h0M39 89h0M40 89h0M41 89.3h0M42 86.5h0M43 85.4h0M44 86.4h0M45 87.3h0M46 87.6h0M47 88h0"/>
    </g>
    <g stroke="var(--usa)">
      <polyline vector-effect="non-scaling-stroke" stroke-width="1.2" points="0,42 1,39.5 2,38.3 3,38.5 4,39.5 5,39.5 6,40.5 7,38 8,37 9,35 10,35.5 11,35 12,34 13,32 14,33.8 15,33 16,32 17,32 18,29.5 19,31 20,30.6 21,29.8 22,31.5 23,33.5 24,34.5 25,33.2 26,33 27,33.3 28,35 29,35.8 30,36.8 31,36.7 32,36.7 33,37 34,35.7 35,35.5 36,36 37,36.8 38,36.7 39,38 40,38 41,37.7 42,40.5 43,41.3 44,40.5 45,39.5 46,39.2 47,38.8"/>
      <path vector-effect="non-scaling-stroke" stroke-width="4.5" stroke-linecap="round" d="M0 42h0M1 39.5h0M2 38.3h0M3 38.5h0M4 39.5h0M5 39.5h0M6 40.5h0M7 38h0M8 37h0M9 35h0M10 35.5h0M11 35h0M12 34h0M13 32h0M14 33.8h0M15 33h0M16 32h0M17 32h0M18 29.5h0M19 31h0M20 30.6h0M21 29.8h0M22 31.5h0M23 33.5h0M24 34.5h0M25 33.2h0M26 33h0M27 33.3h0M28 35h0M29 35.8h0M30 36.8h0M31 36.7h0M32 36.7h0M33 37h0M34 35.7h0M35 35.5h0M36 36h0M37 36.8h0M38 36.7h0M39 38h0M40 38h0M41 37.7h0M42 40.5h0M43 41.3h0M44 40.5h0M45 39.5h0M46 39.2h0M47 38.8h0"/>
    </g>
    <g stroke="var(--uk)">
      <polyline vector-effect="non-scaling-stroke" stroke-width="1.2" points="0,19 1,21 2,22.2 3,22 4,21 5,21 6,20 7,22.6 8,23.5 9,25.3 10,24.8 11,25.2 12,26.3 13,28.5 14,26.8 15,27.5 16,28.3 17,28.3 18,31.3 19,29.5 20,30 21,30.8 22,29 23,27 24,26 25,27 26,27.3 27,27 28,25.4 29,24.6 30,23.8 31,24 32,24 33,23.6 34,24.6 35,24.8 36,24.3 37,23.7 38,23.7 39,22.6 40,22.6 41,22.8 42,20 43,19 44,20 45,21 46,21.4 47,21.8"/>
      <path vector-effect="non-scaling-stroke" stroke-width="4.5" stroke-linecap="round" d="M0 19h0M1 21h0M2 22.2h0M3 22h0M4 21h0M5 21h0M6 20h0M7 22.6h0M8 23.5h0M9 25.3h0M10 24.8h0M11 25.2h0M12 26.3h0M13 28.5h0M14 26.8h0M15 27.5h0M16 28.3h0M17 28.3h0M18 31.3h0M19 29.5h0M20 30h0M21 30.8h0M22 29h0M23 27h0M24 26h0M25 27h0M26 27.3h0M27 27h0M28 25.4h0M29 24.6h0M30 23.8h0M31 24h0M32 24h0M33 23.6h0M34 24.6h0M35 24.8h0M36 24.3h0M37 23.7h0M38 23.7h0M39 22.6h0M40 22.6h0M41 22.8h0M42 20h0M43 19h0M44 20h0M45 21h0M46 21.4h0M47 21.8h0"/>
    </g>
    <g stroke="var(--india)">
      <polyline vector-effect="non-scaling-stroke" stroke-width="1.2" points="0,13 1,12.6 2,12.4 3,11.5 4,10.5 5,11.5 6,14.2 7,14 8,14 9,15.1 10,15.1 11,15.8 12,16.3 13,16 14,15 15,15.3 16,15.3 17,15 18,15.7 19,16.5 20,18.5 21,18.6 22,18.3 23,17.3 24,18.2 25,20.3 26,22.3 27,21.2 28,20.7 29,22.9 30,19.7 31,19.6 32,18.7 33,17.9 34,19.7 35,17.5 36,16.5 37,16.2 38,16.7 39,15 40,14.2 41,11.5 42,12.4 43,12.5 44,13.7 45,13.6 46,12.4 47,10"/>
      <path vector-effect="non-scaling-stroke" stroke-width="4.5" stroke-linecap="round" d="M0 13h0M1 12.6h0M2 12.4h0M3 11.5h0M4 10.5h0M5 11.5h0M6 14.2h0M7 14h0M8 14h0M9 15.1h0M10 15.1h0M11 15.8h0M12 16.3h0M13 16h0M14 15h0M15 15.3h0M16 15.3h0M17 15h0M18 15.7h0M19 16.5h0M20 18.5h0M21 18.6h0M22 18.3h0M23 17.3h0M24 18.2h0M25 20.3h0M26 22.3h0M27 21.2h0M28 20.7h0M29 22.9h0M30 19.7h0M31 19.6h0M32 18.7h0M33 17.9h0M34 19.7h0M35 17.5h0M36 16.5h0M37 16.2h0M38 16.7h0M39 15h0M40 14.2h0M41 11.5h0M42 12.4h0M43 12.5h0M44 13.7h0M45 13.6h0M46 12.4h0M47 10h0"/>
    </g>
    <g stroke="var(--china)">
      <polyline vector-effect="non-scaling-stroke" stroke-width="1.2" points="0,1.8 1,4 2,5.3 3,5.3 4,4.3 5,4.1 6,3.2 7,5.8 8,6.7 9,8.6 10,8.3 11,8.5 12,9.5 13,11.5 14,9.9 15,10.7 16,11.6 17,11.6 18,14.5 19,12.6 20,13 21,13.9 22,11.8 23,10 24,9.3 25,10.3 26,10.5 27,10.3 28,8.5 29,8 30,7 31,7.2 32,7.2 33,6.8 34,7.8 35,8.2 36,7.6 37,6.9 38,6.9 39,5.6 40,5.6 41,5.8 42,3.3 43,2.3 44,3.3 45,4.3 46,4.5 47,4.8"/>
      <path vector-effect="non-scaling-stroke" stroke-width="4.5" stroke-linecap="round" d="M0 1.8h0M1 4h0M2 5.3h0M3 5.3h0M4 4.3h0M5 4.1h0M6 3.2h0M7 5.8h0M8 6.7h0M9 8.6h0M10 8.3h0M11 8.5h0M12 9.5h0M13 11.5h0M14 9.9h0M15 10.7h0M16 11.6h0M17 11.6h0M18 14.5h0M19 12.6h0M20 13h0M21 13.9h0M22 11.8h0M23 10h0M24 9.3h0M25 10.3h0M26 10.5h0M27 10.3h0M28 8.5h0M29 8h0M30 7h0M31 7.2h0M32 7.2h0M33 6.8h0M34 7.8h0M35 8.2h0M36 7.6h0M37 6.9h0M38 6.9h0M39 5.6h0M40 5.6h0M41 5.8h0M42 3.3h0M43 2.3h0M44 3.3h0M45 4.3h0M46 4.5h0M47 4.8h0"/>
    </g>
  </g>
  <g font-size="14.5" text-decoration="underline">
    <text x="1239" y="563" fill="var(--brazil)">Brazil</text>
    <text x="1239" y="799" fill="var(--usa)">United</text><text x="1239" y="818" fill="var(--usa)">States</text>
    <text x="1239" y="883" fill="var(--uk)">United</text><text x="1239" y="902" fill="var(--uk)">Kingdom</text>
    <text x="1239" y="938" fill="var(--india)">India</text>
    <text x="1239" y="964" fill="var(--china)">China</text>
  </g>
</svg>

<div class="dl abs" style="left:52px">Download as PNG</div>
<div class="dl abs" style="left:249px">Download as SVG</div>
<div class="share abs">
  <span>Share this data</span>
  <span class="net"><span class="dot"></span>Circlely</span>
  <span class="net"><span class="dot"></span>Chirpnet</span>
  <svg width="26" height="20" viewBox="0 0 26 20" fill="none" stroke="#0e2a47" stroke-width="2" stroke-linecap="round"><path d="M7 4 1 10l6 6M19 4l6 6-6 6M15 2 11 18"/></svg>
</div>

<h2 class="section-title serif abs" style="left:52px;top:1165px">Energy sources</h2>
<div class="hint abs" style="left:265px;top:1174px">Select an energy source to view its data in the chart</div>

<div class="box abs" style="left:52px;top:1213px;width:1258px;height:70px"></div>
<div class="opt" style="left:95px;top:1236px"><span class="radio"></span>Electricity</div>

<div class="box abs" style="left:52px;top:1298px;width:622px;height:252px"></div>
<div class="box abs" style="left:690px;top:1298px;width:405px;height:252px"></div>
<div class="box abs" style="left:1110px;top:1298px;width:200px;height:252px"></div>

<div class="opt" style="left:95px;top:1330px"><span class="radio on"></span>Low-carbon Energy</div>
<div class="opt" style="left:130px;top:1376px"><span class="radio"></span>Hydro</div>
<div class="opt" style="left:130px;top:1413px"><span class="radio"></span>Nuclear</div>
<div class="opt" style="left:337px;top:1376px"><span class="radio"></span>Wind, Solar &amp; Other-renewables</div>
<div class="opt" style="left:372px;top:1421px"><span class="radio"></span>Wind</div>
<div class="opt" style="left:372px;top:1458px"><span class="radio"></span>Solar</div>
<div class="opt" style="left:372px;top:1495px"><span class="radio"></span>Other-renewables</div>

<div class="opt" style="left:732px;top:1330px"><span class="radio"></span>Fossil Fuels</div>
<div class="opt" style="left:767px;top:1376px"><span class="radio"></span>Coal</div>
<div class="opt" style="left:767px;top:1413px"><span class="radio"></span>Oil</div>
<div class="opt" style="left:767px;top:1450px"><span class="radio"></span>Gas</div>
<div class="opt" style="left:767px;top:1487px"><span class="radio"></span>Unspecified Fossil Fuels</div>

<div class="opt" style="left:1152px;top:1330px"><span class="radio"></span>Other</div>

<section class="regions abs"></section>
<h2 class="section-title serif abs" style="left:94px;top:1620px">5 selected countries and regions</h2>
<div class="reg-search abs">Search region
  <svg class="abs" style="right:12px;top:8px" width="18" height="18" viewBox="0 0 18 18" fill="none" stroke="#0e2a47" stroke-width="1.8"><circle cx="7.5" cy="7.5" r="5.5"/><line x1="11.5" y1="11.5" x2="16" y2="16" stroke-linecap="round"/></svg>
</div>
<div class="reg-sort abs">Region’s Progress
  <svg class="abs" style="right:14px;top:12px" width="12" height="8" viewBox="0 0 12 8" fill="none" stroke="#0e2a47" stroke-width="2"><path d="M1 1l5 5 5-5"/></svg>
</div>
<div class="opt" style="left:1038px;top:1628px;gap:15px"><span class="check"></span>Select all</div>
<div class="opt" style="left:1158px;top:1628px;gap:12px"><svg width="18" height="18" viewBox="0 0 18 18" stroke="#0e2a47" stroke-width="3"><path d="M2 2l14 14M16 2 2 16"/></svg>Unselect all</div>

<div class="col" style="left:95px">
  <div><span class="check on"><svg width="14" height="11" viewBox="0 0 14 11" fill="none" stroke="#fff" stroke-width="2.4"><path d="M1 5.5l4 4L13 1"/></svg></span>United States</div>
  <div><span class="check on"><svg width="14" height="11" viewBox="0 0 14 11" fill="none" stroke="#fff" stroke-width="2.4"><path d="M1 5.5l4 4L13 1"/></svg></span>United Kingdom</div>
  <div><span class="check on"><svg width="14" height="11" viewBox="0 0 14 11" fill="none" stroke="#fff" stroke-width="2.4"><path d="M1 5.5l4 4L13 1"/></svg></span>China</div>
  <div><span class="check on"><svg width="14" height="11" viewBox="0 0 14 11" fill="none" stroke="#fff" stroke-width="2.4"><path d="M1 5.5l4 4L13 1"/></svg></span>India</div>
  <div><span class="check on"><svg width="14" height="11" viewBox="0 0 14 11" fill="none" stroke="#fff" stroke-width="2.4"><path d="M1 5.5l4 4L13 1"/></svg></span>Brazil</div>
  <div><span class="check"></span>Antigua and Barbuda</div>
  <div><span class="check"></span>Argentina</div>
</div>
<div class="col" style="left:340px">
  <div><span class="check"></span>Afghanistan</div><div><span class="check"></span>Albania</div><div><span class="check"></span>Algeria</div><div><span class="check"></span>Andorra</div><div><span class="check"></span>Angola</div><div><span class="check"></span>Antigua and Barbuda</div><div><span class="check"></span>Argentina</div>
</div>
<div class="col" style="left:585px">
  <div><span class="check"></span>Afghanistan</div><div><span class="check"></span>Albania</div><div><span class="check"></span>Algeria</div><div><span class="check"></span>Andorra</div><div><span class="check"></span>Angola</div><div><span class="check"></span>Antigua and Barbuda</div><div><span class="check"></span>Argentina</div>
</div>
<div class="col" style="left:830px">
  <div><span class="check"></span>Afghanistan</div><div><span class="check"></span>Albania</div><div><span class="check"></span>Algeria</div><div><span class="check"></span>Andorra</div><div><span class="check"></span>Angola</div><div><span class="check"></span>Antigua and Barbuda</div><div><span class="check"></span>Argentina</div>
</div>
<div class="col" style="left:1057px">
  <div><span class="check"></span>Afghanistan</div><div><span class="check"></span>Albania</div><div><span class="check"></span>Algeria</div><div><span class="check"></span>Andorra</div><div><span class="check"></span>Angola</div><div><span class="check"></span>Antigua and Barbuda</div><div><span class="check"></span>Argentina</div>
</div>
<div class="scroll-track abs"></div>
<div class="scroll-thumb abs"></div>

<section class="concl">
  <h2 class="section-title serif abs" style="left:52px;top:2032px">The most important general conclusions that can be drawn from the data</h2>
  <p class="abs" style="left:52px;top:2083px;width:1260px">Lorem ipsum dolor sit amet, consectetur adipiscing elit. Aliquam et nibh porta ante pretium finibus. Vivamus ultricies quam eu orci gravida, vel fermentum orci tincidunt. In egestas pharetra sem id sodales. Pellentesque tristique pulvinar urna, in tristique magna mollis ac. Etiam eget ex hendrerit velit blandit porta. Phasellus sed interdum nisl.</p>
  <ul class="bullets abs" style="left:52px;top:2170px;width:620px">
    <li>The world as a whole is NOT moving away from fossil fuels for electricity generation.</li>
    <li>There are substantial differences between energy sources. Regions that have successfully decarbonized their electricity generation have usually done so using hydro and/or nuclear. Other low-carbon energy sources have grown quickly in relative terms in the last few years but are so far contributing little in absolute numbers.</li>
  </ul>
  <ul class="bullets abs" style="left:694px;top:2170px;width:616px">
    <li>There are substantial differences between regions.</li>
    <li class="sub">Some regions have basically solved the problem – they already generate almost all of their electricity from non-fossil sources.</li>
    <li class="sub">Some regions have greatly improved in terms of decarbonizing their electricity generation.</li>
    <li class="sub">Some regions have greatly deteriorated, in other words they are using a much higher share of fossil fuels to generate their electricity.</li>
  </ul>
</section>

<footer>
  <div class="footer abs" style="left:52px">Data source: &nbsp;<a>The Tessary Trust</a> , &nbsp;<a>KQ</a></div>
  <div class="footer abs" style="right:52px;font-weight:700">For any questions please feel free to email me at <a class="mail" style="font-weight:400">o@vantorgrid.net</a></div>
</footer>

</div>
</body>
</html>
```